Marnick Building Materials letterhead template

Simple but professional letterhead template for business communication.
LOGO/name in upper left, balanced by company contact info on right upper.
Subject description, date...
addressee, cc: and BC: if applicable editable info..

Need extra days to review

```html
<!DOCTYPE html>
<html lang="en">
<head>
<meta charset="utf-8">
<title>Marnick Building Materials – Stationery</title>
<link rel="stylesheet" href="https://fonts.googleapis.com/css2?family=Bodoni+Moda:wght@400&family=Poppins:wght@400;500;600;700&display=swap">
<style>
  :root {
    --brand-blue: #2960ae;
    --flap-blue: #2a62b0;
    --ink: #1b1b1b;
    --paper: #ffffff;
    --tint: #f0f1f8;
    --backdrop: #cdd4d5;
  }
  * { margin: 0; padding: 0; box-sizing: border-box; }
  html, body { width: 1200px; height: 842px; overflow: hidden; }
  body {
    position: relative;
    background: var(--backdrop);
    font-family: "Poppins", sans-serif;
    color: var(--ink);
  }
  .piece { position: absolute; overflow: hidden; }
  .label {
    position: absolute;
    font-family: "Bodoni Moda", serif;
    font-size: 27px;
    color: #1e1e1e;
    transform: translateX(-50%);
    white-space: nowrap;
  }
  .brand-name {
    position: absolute;
    font-weight: 700;
    text-transform: uppercase;
    letter-spacing: 0.06em;
    line-height: 1.12;
    color: var(--brand-blue);
  }
  .brand-square { position: absolute; background: var(--brand-blue); border-radius: 4px; }
  .tint-circle { position: absolute; border-radius: 50%; background: var(--tint); }
  .icon { width: 1em; height: 1em; fill: var(--brand-blue); vertical-align: -0.12em; }

  /* Letterhead */
  .letterhead { left: 111px; top: 65px; width: 497px; height: 702px; background: var(--paper); }
  .letterhead .brand-square { left: 26px; top: 27px; width: 66px; height: 66px; border-radius: 10px; }
  .letterhead .brand-name { left: 113px; top: 23px; font-size: 20px; }
  .letterhead .contact-list {
    position: absolute; right: 26px; top: 34px;
    list-style: none; text-align: right; font-size: 10.5px; line-height: 13px;
  }
  .letterhead .contact-list .icon { margin-left: 7px; }
  .letterhead .date-line { position: absolute; left: 28px; top: 133px; font-size: 9px; }
  .letterhead .subject-line {
    position: absolute; left: 28px; top: 149px;
    font-size: 11px; font-weight: 600; color: var(--brand-blue);
  }
  .letterhead .tint-circle { left: 82px; top: 266px; width: 300px; height: 300px; }

  /* Business card */
  .card-front {
    left: 731px; top: 65px; width: 277px; height: 158px;
    border-radius: 10px; background: var(--brand-blue);
  }
  .card-front .brand-square { left: 40px; top: 46px; width: 66px; height: 66px; border-radius: 10px; background: var(--paper); }
  .card-front .brand-name { left: 122px; top: 44px; font-size: 18.5px; color: var(--paper); }

  .card-back {
    left: 731px; top: 239px; width: 277px; height: 158px;
    border-radius: 10px; background: var(--paper);
  }
  .card-back .tint-circle { left: 90px; top: 5px; width: 170px; height: 170px; }
  .card-back .brand-square { left: 11px; top: 10px; width: 47px; height: 43px; border-radius: 7px; }
  .card-back .brand-name { left: 64px; top: 9px; font-size: 11px; line-height: 14.5px; }
  .person-bar { position: absolute; left: 0; top: 70px; width: 7px; height: 24px; background: var(--brand-blue); }
  .person-name {
    position: absolute; left: 10px; top: 68px;
    font-size: 16px; line-height: 18px; color: var(--brand-blue);
  }
  .person-name strong { font-weight: 600; }
  .person-role { position: absolute; left: 10px; top: 86px; font-size: 7px; }
  .address {
    position: absolute; font-size: 7px; line-height: 9.3px;
    color: var(--brand-blue); font-weight: 500;
  }
  .card-back .address { left: 10px; top: 100px; }
  .contact-rows { position: absolute; list-style: none; font-size: 7.2px; line-height: 9.5px; }
  .contact-rows .icon { margin-right: 4px; }
  .card-back .contact-rows { left: 10px; top: 122px; }

  /* Envelope */
  .envelope-front { left: 687px; top: 423px; width: 372px; height: 166px; background: var(--paper); }
  .envelope-front .tint-circle { left: 172px; top: 4px; width: 190px; height: 190px; }
  .envelope-front .brand-square { left: 6px; top: 9px; width: 45px; height: 40px; border-radius: 8px; }
  .envelope-front .brand-name { left: 55px; top: 7px; font-size: 11px; line-height: 13.5px; }
  .envelope-front .address { left: 20px; top: 104px; padding-left: 0; }
  .envelope-front .address-pin { position: absolute; left: 6px; top: 106px; font-size: 9px; }
  .envelope-front .contact-rows { left: 6px; top: 129px; font-size: 7.5px; }

  .envelope-back { left: 687px; top: 606px; width: 372px; height: 166px; background: var(--brand-blue); }
  .envelope-flap {
    position: absolute; left: 3px; top: 0; width: 366px; height: 56px;
    background: var(--flap-blue); border-radius: 0 0 14px 14px;
    box-shadow: 0 2px 3px rgba(20, 50, 100, 0.35);
  }
  .envelope-flap .flap-name {
    position: absolute; left: 50%; top: 22px; transform: translateX(-50%);
    font-size: 8px; font-weight: 700; letter-spacing: 0.08em; color: var(--paper);
  }
</style>
</head>
<body>
<svg width="0" height="0" style="position:absolute" aria-hidden="true">
  <symbol id="i-phone" viewBox="0 0 24 24"><path d="M6.6 10.8a15 15 0 0 0 6.6 6.6l2.2-2.2a1 1 0 0 1 1-.25 11.4 11.4 0 0 0 3.6.6 1 1 0 0 1 1 1V20a1 1 0 0 1-1 1A17 17 0 0 1 3 4a1 1 0 0 1 1-1h3.5a1 1 0 0 1 1 1c0 1.25.2 2.45.6 3.6a1 1 0 0 1-.25 1z"/></symbol>
  <symbol id="i-globe" viewBox="0 0 24 24"><path d="M12 2a10 10 0 1 0 0 20 10 10 0 0 0 0-20zm-1 17.9A8 8 0 0 1 4.1 10.4L9 15.3v1a2 2 0 0 0 2 2zm6.9-2.5A2 2 0 0 0 16 16h-1v-3a1 1 0 0 0-1-1H8v-2h2a1 1 0 0 0 1-1V7h2a2 2 0 0 0 2-2v-.4a8 8 0 0 1 2.9 12.8z"/></symbol>
  <symbol id="i-mail" viewBox="0 0 24 24"><path d="M3 5h18a1 1 0 0 1 1 1v12a1 1 0 0 1-1 1H3a1 1 0 0 1-1-1V6a1 1 0 0 1 1-1zm1 2.4V17h16V7.4l-8 5.6z"/></symbol>
  <symbol id="i-pin" viewBox="0 0 24 24"><path d="M12 2a7 7 0 0 0-7 7c0 5.2 7 13 7 13s7-7.8 7-13a7 7 0 0 0-7-7zm0 9.5A2.5 2.5 0 1 1 12 6.5a2.5 2.5 0 0 1 0 5z"/></symbol>
</svg>

<div class="label" style="left:857px;top:14px;">Business card</div>

<section class="piece letterhead">
  <div class="tint-circle"></div>
  <div class="brand-square"></div>
  <div class="brand-name">Marnick<br>Building<br>Materials</div>
  <ul class="contact-list">
    <li>1-805-555-0142<svg class="icon"><use href="#i-phone"/></svg></li>
    <li>info@marnick-bm.com<svg class="icon"><use href="#i-globe"/></svg></li>
    <li>www.marnick-bm.com<svg class="icon"><use href="#i-mail"/></svg></li>
  </ul>
  <p class="date-line">Date:-</p>
  <p class="subject-line">Subject:-</p>
</section>
<div class="label" style="left:346px;top:778px;">Letterhead</div>

<section class="piece card-front">
  <div class="brand-square"></div>
  <div class="brand-name">Marnick<br>Building<br>Materials</div>
</section>

<section class="piece card-back">
  <div class="tint-circle"></div>
  <div class="brand-square"></div>
  <div class="brand-name">Marnick<br>Building<br>Materials</div>
  <div class="person-bar"></div>
  <p class="person-name"><strong>Dana</strong> Whitlow</p>
  <p class="person-role">Founder &amp; CEO</p>
  <p class="address">48 Harbor View Rd.<br>Fairport, CA 93190</p>
  <ul class="contact-rows">
    <li><svg class="icon"><use href="#i-phone"/></svg>1-805-555-0142</li>
    <li><svg class="icon"><use href="#i-globe"/></svg>info@marnick-bm.com</li>
    <li><svg class="icon"><use href="#i-mail"/></svg>www.marnick-bm.com</li>
  </ul>
</section>

<section class="piece envelope-front">
  <div class="tint-circle"></div>
  <div class="brand-square"></div>
  <div class="brand-name">Marnick<br>Building<br>Materials</div>
  <svg class="icon address-pin"><use href="#i-pin"/></svg>
  <p class="address">48 Harbor View Rd.<br>Fairport, CA 93190</p>
  <ul class="contact-rows">
    <li><svg class="icon"><use href="#i-phone"/></svg>1-805-555-0142</li>
    <li><svg class="icon"><use href="#i-globe"/></svg>info@marnick-bm.com</li>
    <li><svg class="icon"><use href="#i-mail"/></svg>www.marnick-bm.com</li>
  </ul>
</section>

<section class="piece envelope-back">
  <div class="envelope-flap"><span class="flap-name">MARNICK</span></div>
</section>
<div class="label" style="left:885px;top:781px;">Envelope</div>
</body>
</html>
```